Banner Ad Design Project for responsive website

Looking to update the main banner on my website www.vowlantern.example but it will be for our new responsive website, you can see here http://www.vowlantern.example/dev/
Banner should be 300 px high by1920 pix wide
Please contact me with any questions
Should include:
All the text from the existing banner ie
Bridal Show
THE FIRST 50 BRIDES WILL GET A CHANCE TO WIN $25000
Honeymoon Cruise Giveaway
"Pick Your Perfect Gown" casting call
Banner should be 1920 pix wide
Final delivery will require layered psd file and all fonts

Target Market(s)

Brides

Industry/Entity Type

Call

Requirements
Must have
• All the text from the existing banner ie
• Bridal Show
• THE FIRST 50 BRIDES WILL GET A CHANCE TO WIN $25000
• Honeymoon Cruise Giveaway
• "Pick Your Perfect Gown" casting call
• Banner should be 1920 pix wide
Nice to have
• The look and feel of our postcard, see attached
Should not have
• Any specifics to any date/time/location as the banner will be online all the time and the specifics for each show will be different

```html
<!DOCTYPE html>
<html lang="en">
<head>
<meta charset="utf-8">
<title>Bridal Show Casting Call Banner</title>
<link rel="stylesheet" href="https://fonts.googleapis.com/css2?family=Alfa+Slab+One&family=Arimo:wght@400;700&family=Great+Vibes&display=swap">
<style>
  :root {
    --page-bg: #ecebe8;
    --banner-white: #f7f7f5;
    --lace-grey: #e4e4e2;
    --ink: #111111;
    --script-green: #1f7a22;
    --money-green: #1d7a1d;
    --script-blue: #5a9fd6;
    --rule-blue: #8fbfe3;
    --photo-light: #e9e4c6;
    --photo-green: #6f8b4a;
    --photo-deep: #3f5a2c;
    --sea-blue: #2f6fb0;
    --sky-blue: #a9cdea;
    --ornament-green: #cfe3c7;
  }
  * { margin: 0; padding: 0; box-sizing: border-box; }
  html, body {
    width: 1200px;
    height: 900px;
    overflow: hidden;
    background: var(--page-bg);
  }
  .banner {
    position: absolute;
    left: 20px;
    top: 197px;
    width: 1160px;
    height: 506px;
    overflow: hidden;
    background: radial-gradient(ellipse at 65% 55%, var(--banner-white) 0%, var(--lace-grey) 100%);
    font-family: "Arimo", Arial, sans-serif;
    color: var(--ink);
  }
  .lace-texture {
    position: absolute;
    inset: 0;
    background: linear-gradient(160deg, rgba(255,255,255,0.7) 0%, rgba(228,228,226,0.5) 60%, rgba(255,255,255,0.6) 100%);
  }
  .bride-photo {
    position: absolute;
    left: 0;
    top: 0;
    width: 460px;
    height: 506px;
  }
  .bell-ornament {
    position: absolute;
    top: 4px;
    width: 70px;
    height: 54px;
    border-radius: 50%;
    background: var(--ornament-green);
  }
  .bell-ornament--left { left: 425px; }
  .bell-ornament--right { left: 985px; }
  .show-title {
    position: absolute;
    left: 450px;
    width: 500px;
    top: 0;
    text-align: center;
    font-family: "Great Vibes", cursive;
    font-size: 66px;
    line-height: 80px;
    color: var(--script-green);
    font-weight: 400;
  }
  .casting-call {
    position: absolute;
    left: 450px;
    width: 500px;
    top: 92px;
    text-align: center;
    font-size: 23px;
  }
  .tagline {
    position: absolute;
    left: 400px;
    width: 600px;
    top: 130px;
    text-align: center;
    font-size: 35px;
  }
  .tagline .script {
    font-family: "Great Vibes", cursive;
    font-size: 42px;
    color: var(--script-blue);
  }
  .rule {
    position: absolute;
    height: 1px;
    background: var(--rule-blue);
  }
  .rule--top { left: 486px; width: 594px; top: 198px; }
  .rule--bottom { left: 486px; width: 630px; top: 382px; }
  .offer {
    position: absolute;
    left: 400px;
    width: 790px;
    top: 208px;
    text-align: center;
    font-family: "Alfa Slab One", serif;
    font-size: 39px;
    line-height: 44px;
    letter-spacing: 1px;
  }
  .offer .highlight { color: var(--money-green); }
  .station-mark {
    position: absolute;
    left: 385px;
    top: 398px;
    display: flex;
    align-items: center;
    gap: 10px;
    font-size: 30px;
    font-weight: 700;
    color: var(--ink);
  }
  .station-mark .dot {
    width: 26px;
    height: 26px;
    border-radius: 50%;
    background: var(--script-green);
  }
  .cruise-photo {
    position: absolute;
    left: 947px;
    top: 362px;
    width: 131px;
    height: 78px;
    border-radius: 50%;
    background: linear-gradient(180deg, var(--sky-blue) 0%, var(--sky-blue) 45%, var(--sea-blue) 100%);
  }
  .cruise-caption {
    position: absolute;
    left: 880px;
    width: 270px;
    top: 454px;
    text-align: center;
    font-family: "Great Vibes", cursive;
    font-size: 26px;
    color: var(--script-green);
  }
</style>
</head>
<body>
  <section class="banner">
    <div class="lace-texture" role="img" aria-label="Soft white lace and satin rose fabric background"></div>

    <svg class="bride-photo" viewBox="0 0 460 506" role="img" aria-label="Photo of a smiling bride in a strapless white gown and veil standing outdoors in sunlit greenery">
      <defs>
        <linearGradient id="garden-light" x1="0" y1="0" x2="1" y2="1">
          <stop offset="0" stop-color="var(--photo-deep)"/>
          <stop offset="0.45" stop-color="var(--photo-green)"/>
          <stop offset="0.8" stop-color="var(--photo-light)"/>
          <stop offset="1" stop-color="var(--photo-green)"/>
        </linearGradient>
      </defs>
      <path d="M0 0 H333 Q440 230 274 506 H0 Z" fill="url(#garden-light)"/>
    </svg>

    <div class="bell-ornament bell-ornament--left" role="img" aria-label="Wedding bells ornament"></div>
    <div class="bell-ornament bell-ornament--right" role="img" aria-label="Wedding bells ornament"></div>

    <h1 class="show-title">Bridal Show</h1>
    <p class="casting-call">Casting Call</p>
    <p class="tagline">Pick <span class="script">Your</span> Perfect <span class="script">Gown</span></p>

    <div class="rule rule--top"></div>
    <p class="offer">THE FIRST <span class="highlight">50</span> BRIDES WILL<br>GET A CHANCE TO WIN<br><span class="highlight">$25,000</span></p>
    <div class="rule rule--bottom"></div>

    <div class="station-mark"><span class="dot"></span>Harbor 94</div>

    <div class="cruise-photo" role="img" aria-label="Photo of a cruise ship at sea"></div>
    <p class="cruise-caption">Honeymoon Cruise Giveaway</p>
  </section>
</body>
</html>
```